Business Card

We would like a very clean corporate, two sided business card that conveys that we are a quality focused, reliable organisation that can make a business better. We focus on a cycle of continuous improvement for IT systems.

The brief is primarily clean and corporate, nothing overly complicated.

We sell IT services, IT support, server implementation, problem solving services to businesses in Australia.

Business

```html
<!DOCTYPE html>
<html lang="en">
<head>
<meta charset="utf-8">
<title>Nexacore – Business Card Options</title>
<link href="https://fonts.googleapis.com/css2?family=Poppins:wght@600&family=Archivo+Narrow:wght@400;500&family=Arimo:wght@400&display=swap" rel="stylesheet">
<style>
  :root{
    --ink:#3a3a3a;
    --black:#111;
    --red:#d7242c;
    --yellow:#f3e22a;
    --grey-dark:#a9a9a9;
    --grey-mid:#cfcfcf;
    --grey-light:#f1f1f1;
    --white:#fff;
  }
  *{box-sizing:border-box;margin:0;padding:0}
  html,body{width:1200px;height:752px;overflow:hidden;background:var(--white)}
  .sheet{position:relative;width:1200px;height:752px}

  .card{position:absolute;overflow:hidden;color:var(--black)}
  .card--front{width:392px;height:220px}
  .card--back{width:392px;height:236px}

  /* surfaces */
  .surface-soft{background:linear-gradient(90deg,var(--grey-mid),var(--white) 85%)}
  .surface-steel{background:linear-gradient(90deg,var(--grey-dark),var(--grey-light) 90%)}
  .surface-white{background:var(--white)}
  .surface-mist{background:var(--grey-light)}

  /* edges */
  .edge-red-top{border-top:4px solid var(--red)}
  .edge-red{border-top:5px solid var(--red);border-bottom:5px solid var(--red)}
  .edge-black-top{border-top:4px solid var(--black)}
  .edge-black{border-top:4px solid var(--black);border-bottom:4px solid var(--black)}
  .edge-black-frame{border:1px solid #999;border-top:4px solid var(--black);border-bottom:3px solid var(--black)}
  .edge-yellow{border-top:5px solid var(--yellow);border-bottom:5px solid var(--yellow)}
  .edge-yellow-frame{border:1px solid #bbb;border-top:5px solid var(--yellow);border-bottom:5px solid var(--yellow)}

  /* brand lockup */
  .brand{position:absolute;display:flex;align-items:center;gap:10px}
  .brand__name{font-family:"Poppins",sans-serif;font-weight:600;font-size:30px;letter-spacing:-0.5px;color:var(--ink);line-height:1}
  .brand__mark{width:22px;height:22px;background:var(--red)}
  .tagline{position:absolute;font-family:"Archivo Narrow",sans-serif;font-weight:500;font-size:20px;color:var(--black);white-space:nowrap}

  .card--front .brand{left:100px;top:20px}
  .card--front .tagline{left:100px;top:60px}
  .card--back .brand{left:16px;top:16px}
  .card--back .tagline{left:16px;top:56px}

  /* contact details */
  .address{position:absolute;left:0;right:0;top:146px;text-align:center;font-family:"Arimo",sans-serif;font-size:10px;line-height:1.35;color:var(--black)}
  .contacts{position:absolute;left:16px;right:16px;bottom:14px;display:flex;justify-content:space-between;font-family:"Arimo",sans-serif;font-size:10px;color:var(--black)}

  /* services */
  .services{position:absolute;left:176px;top:112px;display:grid;grid-template-columns:auto auto;column-gap:2px;font-family:"Archivo Narrow",sans-serif;color:var(--black)}
  .services__it{font-family:"Arimo",sans-serif;font-size:62px;line-height:0.82;color:var(--red);grid-row:1 / span 2}
  .services__item{font-size:23px;line-height:1.05}
  .services__item--indent{padding-left:22px}
  .services__item--wide{grid-column:1 / span 2;margin-top:2px}
</style>
</head>
<body>
<main class="sheet">

  <!-- Row 1: fronts -->
  <section class="card card--front surface-soft edge-red-top" style="left:4px;top:4px">
    <div class="brand"><span class="brand__name">nexacore</span><span class="brand__mark"></span></div>
    <p class="tagline">Systems that work better</p>
    <p class="address">Nexacore Pty Ltd, Suite 210, 14-18 Harlow Street, Eastwood Point, NSW, 2099<br>Australia</p>
    <p class="contacts"><span>PH: +61 2 9555 0142</span><span>FAX: +61 2 9555 0143</span><span>ABN: 48 123 456 789</span></p>
  </section>

  <section class="card card--front surface-steel edge-black-top" style="left:410px;top:4px">
    <div class="brand"><span class="brand__name">nexacore</span><span class="brand__mark"></span></div>
    <p class="tagline">Systems that work better</p>
    <p class="address">Nexacore Pty Ltd, Suite 210, 14-18 Harlow Street, Eastwood Point, NSW, 2099<br>Australia</p>
    <p class="contacts"><span>PH: +61 2 9555 0142</span><span>FAX: +61 2 9555 0143</span><span>ABN: 48 123 456 789</span></p>
  </section>

  <section class="card card--front surface-white edge-black-top" style="left:808px;top:4px">
    <div class="brand"><span class="brand__name">nexacore</span><span class="brand__mark"></span></div>
    <p class="tagline">Systems that work better</p>
    <p class="address">Nexacore Pty Ltd, Suite 210, 14-18 Harlow Street, Eastwood Point, NSW, 2099<br>Australia</p>
    <p class="contacts"><span>PH: +61 2 9555 0142</span><span>FAX: +61 2 9555 0143</span><span>ABN: 48 123 456 789</span></p>
  </section>

  <!-- Row 2: backs -->
  <section class="card card--back surface-steel edge-red" style="left:4px;top:230px">
    <div class="brand"><span class="brand__name">nexacore</span><span class="brand__mark"></span></div>
    <p class="tagline">Systems that work better</p>
    <div class="services">
      <span class="services__it">IT</span>
      <span class="services__item">Consulting</span>
      <span class="services__item services__item--indent">Outsourcing</span>
      <span class="services__item services__item--wide">Managed Services</span>
    </div>
  </section>

  <section class="card card--back surface-steel edge-black" style="left:410px;top:230px">
    <div class="brand"><span class="brand__name">nexacore</span><span class="brand__mark"></span></div>
    <p class="tagline">Systems that work better</p>
    <div class="services">
      <span class="services__it">IT</span>
      <span class="services__item">Consulting</span>
      <span class="services__item services__item--indent">Outsourcing</span>
      <span class="services__item services__item--wide">Managed Services</span>
    </div>
  </section>

  <section class="card card--back surface-white edge-black-frame" style="left:808px;top:230px">
    <div class="brand"><span class="brand__name">nexacore</span><span class="brand__mark"></span></div>
    <p class="tagline">Systems that work better</p>
    <div class="services">
      <span class="services__it">IT</span>
      <span class="services__item">Consulting</span>
      <span class="services__item services__item--indent">Outsourcing</span>
      <span class="services__item services__item--wide">Managed Services</span>
    </div>
  </section>

  <!-- Row 3: yellow pair -->
  <section class="card card--front surface-mist edge-yellow" style="left:4px;top:528px">
    <div class="brand"><span class="brand__name">nexacore</span><span class="brand__mark"></span></div>
    <p class="tagline">Systems that work better</p>
    <p class="address">Nexacore Pty Ltd, Suite 210, 14-18 Harlow Street, Eastwood Point, NSW, 2099<br>Australia</p>
    <p class="contacts"><span>PH: +61 2 9555 0142</span><span>FAX: +61 2 9555 0143</span><span>ABN: 48 123 456 789</span></p>
  </section>

  <section class="card card--front surface-white edge-yellow-frame" style="left:484px;top:528px;width:396px">
    <div class="brand" style="left:20px;top:16px"><span class="brand__name">nexacore</span><span class="brand__mark"></span></div>
    <p class="tagline" style="left:20px;top:56px">Systems that work better</p>
    <div class="services" style="top:104px;left:180px">
      <span class="services__it">IT</span>
      <span class="services__item">Consulting</span>
      <span class="services__item services__item--indent">Outsourcing</span>
      <span class="services__item services__item--wide">Managed Services</span>
    </div>
  </section>

</main>
</body>
</html>
```